R.T. Framecraft Postcard Design

We need a postcard designed around the utility rebates for window installations. For customers who have Electric heated homes can receive $6 per square foot for each window and patio door and for Natural gas heated homes, they can get $75.00 per window and patio door. The $6 per square foot for electric heated customers is the better rebate averaging about $1000.00 for a house with 10 windows and a patio door. Our Company colors are maroon, black and white, we would like to have a post card designed around these colors. The postcard should be designed to share about these 2 rebates and having a window installation theme. You can use pictures off of our website...www.rtframecraft.example

Target Market(s)

Homeowners with electric heat or Natural gas heat

Industry/Entity Type

Utility

Requirements
Must have
• Blank white square on the back for me to hand write address information.

```html
<!DOCTYPE html>
<html lang="en">
<head>
<meta charset="utf-8">
<title>RT Framecraft Rebate Postcard</title>
<link rel="stylesheet" href="https://fonts.googleapis.com/css2?family=Roboto:ital,wght@0,400;0,500;0,700;0,900;1,400;1,700&display=swap">
<style>
  :root{
    --maroon:#7d1a1f;
    --maroon-dark:#5e1216;
    --ink:#1d1b1b;
    --paper:#ffffff;
    --stage:#000000;
    --footer:#231f20;
    --muted:#3a3a3a;
  }
  *{margin:0;padding:0;box-sizing:border-box}
  html,body{width:818px;height:1200px;overflow:hidden;background:var(--stage)}
  body{position:relative;font-family:"Roboto",Arial,sans-serif;color:var(--ink)}
  .card{position:absolute;left:70px;width:678px;height:526px;background:var(--paper);overflow:hidden}
  .card--front{top:67px}
  .card--back{top:620px}
  .abs{position:absolute}

  /* front */
  .front-art{position:absolute;left:0;top:0;width:678px;height:526px}
  .headline-get{left:43px;top:307px;height:31px;padding:0 14px 0 12px;background:var(--ink);color:#fff;font-weight:900;font-size:27px;line-height:31px;clip-path:polygon(6% 0,100% 0,100% 100%,0 100%)}
  .headline-rebates{left:123px;top:291px;font-weight:900;font-size:53px;line-height:1;color:var(--maroon);letter-spacing:.5px}
  .headline-sub{left:58px;top:342px;font-weight:900;font-size:19.5px;letter-spacing:.3px;color:var(--ink)}
  .offer-label{font-weight:700;font-size:15px;color:var(--maroon)}
  .offer-amount{font-weight:700;font-size:44px;line-height:1;color:var(--ink)}
  .offer-note{font-size:12px;color:var(--muted)}
  .offer-unit{position:absolute;left:52px;top:4px;font-size:16px;line-height:15px;color:var(--ink)}
  .offer--gas{left:43px;top:378px}
  .offer--electric{left:253px;top:378px}
  .offer .offer-amount{margin-top:4px}
  .offer .offer-note{margin-top:6px}
  .amount-wrap{position:relative}
  .offer-divider{left:238px;top:384px;width:1.5px;height:82px;background:var(--ink)}
  .brand-mark{left:471px;top:380px;width:44px;height:44px;background:var(--maroon)}
  .brand-name{left:470px;top:430px;font-weight:700;font-size:30px;color:var(--ink);white-space:nowrap}
  .contact-bar{left:0;top:480px;width:678px;height:46px;background:var(--footer);color:#fff;font-size:17px;display:flex;align-items:center;justify-content:center;gap:8px}
  .contact-bar strong{font-weight:700}

  /* back */
  .back-photo{position:absolute;inset:0;background:linear-gradient(90deg,#cfd2cc 0%,#e2e3de 30%,#f1f1ee 55%,#f7f7f5 100%)}
  .quote-mark{left:152px;font-weight:900;font-size:86px;line-height:1;color:var(--maroon)}
  .quote-mark--open{top:34px}
  .quote-mark--close{top:158px}
  .testimonial{left:51px;top:84px;font-style:italic;font-size:15px;line-height:20px;color:var(--ink)}
  .testimonial cite{font-weight:700;font-style:italic}
  .back-mark{left:51px;top:222px;width:58px;height:58px;background:var(--maroon)}
  .back-name{left:50px;top:284px;font-weight:700;font-size:31px;color:var(--ink);white-space:nowrap}
  .back-address{left:51px;top:329px;font-size:15px;line-height:20px;color:var(--ink)}
  .back-contacts{left:51px;top:393px;list-style:none;font-weight:700;font-size:18px;line-height:23px}
  .back-contacts li{display:flex;align-items:center;gap:6px}
  .back-contacts svg{width:13px;height:13px;flex:none}
</style>
</head>
<body>

<section class="card card--front" aria-label="Postcard front">
  <svg class="front-art" viewBox="0 0 678 526" aria-hidden="false">
    <defs>
      <linearGradient id="roomLeft" x1="0" y1="0" x2="1" y2="1">
        <stop offset="0" stop-color="#8a4a2c"/>
        <stop offset="0.5" stop-color="#c9b79b"/>
        <stop offset="1" stop-color="#6f8a4c"/>
      </linearGradient>
      <linearGradient id="roomRight" x1="0" y1="0" x2="1" y2="1">
        <stop offset="0" stop-color="#e8e6d6"/>
        <stop offset="0.5" stop-color="#7fa35a"/>
        <stop offset="1" stop-color="#2f3a2c"/>
      </linearGradient>
    </defs>
    <g role="img" aria-label="Living rooms with large new double-hung windows looking out onto green lawns and trees">
      <rect x="0" y="0" width="340" height="360" fill="url(#roomLeft)"/>
      <rect x="340" y="0" width="338" height="360" fill="url(#roomRight)"/>
    </g>
    <path d="M0 296 C120 248 240 240 380 268 C480 288 580 330 678 352 L678 360 C580 342 480 300 380 282 C240 256 120 262 0 306 Z" fill="var(--maroon)"/>
    <path d="M0 304 C120 260 240 254 380 280 C480 298 580 338 678 358 L678 526 L0 526 Z" fill="#fff"/>
  </svg>

  <div class="abs headline-get">GET</div>
  <div class="abs headline-rebates">REBATES</div>
  <div class="abs headline-sub">FOR WINDOW INSTALLATIONS</div>

  <div class="abs offer offer--gas">
    <div class="offer-label">Natural gas heated homes</div>
    <div class="offer-amount">$75.00</div>
    <div class="offer-note">per window and patio door</div>
  </div>
  <div class="abs offer-divider"></div>
  <div class="abs offer offer--electric">
    <div class="offer-label">Electric heated homes</div>
    <div class="amount-wrap">
      <div class="offer-amount">$6</div>
      <div class="offer-unit">PER<br>SQ.FT.</div>
    </div>
    <div class="offer-note">each window and patio door</div>
  </div>

  <div class="abs brand-mark" aria-hidden="true"></div>
  <div class="abs brand-name">RT Framecraft</div>

  <div class="abs contact-bar">
    <span>www.rtframecraft.example</span><span>|</span><strong>425-555-0148</strong><span>|</span><span>admin@rtframecraft.example</span>
  </div>
</section>

<section class="card card--back" aria-label="Postcard back">
  <div class="back-photo" role="img" aria-label="Faint sunlit window interior fading into a blank white area for a handwritten address"></div>

  <div class="abs quote-mark quote-mark--open">&ldquo;</div>
  <blockquote class="abs testimonial">
    SPLENDID JOB! Thanks again.<br>
    I will be recommending your<br>
    services to my friends and family.<br>
    <cite>- Daniel Morrow Hale</cite>
  </blockquote>
  <div class="abs quote-mark quote-mark--close">&rdquo;</div>

  <div class="abs back-mark" aria-hidden="true"></div>
  <div class="abs back-name">RT FRAMECRAFT</div>
  <address class="abs back-address" style="font-style:normal">
    1420 Cedar Lane NE<br>
    Lakewood, Washington<br>
    98000, United States
  </address>
  <ul class="abs back-contacts">
    <li><svg viewBox="0 0 13 13"><circle cx="6.5" cy="6.5" r="6.5" fill="var(--maroon)"/><circle cx="6.5" cy="6.5" r="3.6" fill="none" stroke="#fff" stroke-width="1.1"/><line x1="2.9" y1="6.5" x2="10.1" y2="6.5" stroke="#fff" stroke-width="1"/></svg>www.rtframecraft.example</li>
    <li><svg viewBox="0 0 13 13"><rect width="13" height="13" rx="2.5" fill="var(--maroon)"/><path d="M4 3 L5.6 3 L6.2 5 L5.2 5.8 C5.8 7 6.4 7.6 7.4 8.2 L8.2 7.2 L10 7.8 L10 9.4 C7 9.6 3.6 6.4 4 3 Z" fill="#fff"/></svg>425-555-0148</li>
    <li><svg viewBox="0 0 13 13"><rect width="13" height="13" rx="2.5" fill="var(--maroon)"/><path d="M2.5 5 C2.5 3 10.5 3 10.5 5 L9 6 L8 5 L5 5 L4 6 Z" fill="#fff"/><rect x="3.5" y="6.5" width="6" height="3.5" rx="1" fill="#fff"/></svg>360-555-0172</li>
    <li><svg viewBox="0 0 13 13"><rect width="13" height="13" rx="2.5" fill="var(--maroon)"/><rect x="2.5" y="4" width="8" height="5.5" fill="#fff"/><path d="M2.5 4 L6.5 7 L10.5 4" fill="none" stroke="var(--maroon)" stroke-width="1"/></svg>admin@rtframecraft.example</li>
  </ul>
</section>

</body>
</html>
```